A SEASON OF EMBERS book cover needed

Hello friends! I'm working toward self-publishing my first novel in the next few months, and I'm looking to have a professional-looking, 6 in x 9 in cover to go along with the ebook release. I’m not looking for much, but the key is that it must look professional. I don’t want decorative fonts, but I also don’t want it to just look like Helvetica or Times New Roman.The text for the cover should be:A TIME FOR GREATNESSKARLIS WILDEI have attached a few images to show you where my head is at. I created a book cover myself on paint that looks horribly amateur, but it draws inspiration from a HPB campaign poster(also attached) where the title of the novel comes from. If you can make that same kind of cover, but make it look professional, that would be amazing! If you have other, simple ideas, I am also very, very open.Attached as well are a couple of simple, recent book covers that I like. That is the kind of thing that I am looking for.If this goes well, I may do a paperback release. In that case, I may need to contact you again for an additional fee to create the rest of the wraparound design. In addition, the book is the first in a projected trilogy, so there may be opportunities for you in the future for sequel covers.About the book: A SEASON OF EMBERS is a gripping, standalone thriller with an exciting take on history, relationships, conspiracy theories, and the current, volatile political state of America. In the present day, new information surrounding the 1963 assassination of Harold P. Brisbane comes to light and Milo Fenwright, a young, best-selling journalist still reconciling his success with his dark past, finds himself more personally connected than he ever could have expected. But the story becomes something even bigger when an assassination attempt on the current demagogic president sends the whole world of journalism into a scramble, and Milo finds himself confronted by an extremely difficult question: Is democracy real, or has it been an illusion fostered by these secretive ‘Stewards of the Union’ since 1776? Travelling across Syria, Canada, and the United States of America, the story becomes more unbelievable—and more personal—as increasingly prominent figures begin to enter Milo’s orbit, intent on keeping their secrets safe by whatever means necessary.

Colors

Designer to choose colors to be used in the design.

Requirements
Must have
• Text
• Simplicity
• Professional look
Should not have
• Cheap fonts
• Complicated images

```html
<!DOCTYPE html>
<html lang="en">
<head>
<meta charset="utf-8">
<title>A Season of Embers — Cover</title>
<link href="https://fonts.googleapis.com/css2?family=Lato:wght@400;700&display=swap" rel="stylesheet">
<style>
  :root {
    --ember-top: #b56d5c;
    --ember-bottom: #cc8a76;
    --band-white: #f1f0ef;
    --band-shade: #dcdcdc;
    --union-top: #5b80c2;
    --union-bottom: #3d5f98;
    --title-blue: #3169c0;
    --ink-white: #ffffff;
    --star: #ececec;
  }
  html, body {
    margin: 0;
    padding: 0;
    width: 800px;
    height: 1200px;
    overflow: hidden;
    background: #ffffff;
  }
  .cover {
    position: relative;
    width: 800px;
    height: 1200px;
    overflow: hidden;
    font-family: "Lato", Arial, sans-serif;
  }
  .field {
    position: absolute;
    left: 0;
    width: 800px;
  }
  .field--ember {
    top: 0;
    height: 490px;
    background:
      radial-gradient(ellipse at 12% 18%, rgba(255,255,255,0.18), transparent 45%),
      linear-gradient(180deg, var(--ember-top), var(--ember-bottom));
  }
  .field--band {
    top: 490px;
    height: 172px;
    background: radial-gradient(ellipse at 50% 50%, var(--band-white), var(--band-shade) 120%);
  }
  .field--union {
    top: 662px;
    height: 538px;
    background:
      radial-gradient(ellipse at 60% 10%, rgba(255,255,255,0.12), transparent 50%),
      linear-gradient(180deg, var(--union-top), var(--union-bottom));
  }
  .stars {
    position: absolute;
    left: 0;
    top: 0;
    width: 800px;
    height: 1200px;
  }
  .stars .star { fill: var(--star); }
  .book-title { margin: 0; }
  .line {
    position: absolute;
    left: 0;
    width: 800px;
    margin: 0;
    text-align: center;
    line-height: 1;
    white-space: nowrap;
    color: var(--ink-white);
  }
  .title-a      { top: -8px;   font-size: 167px; font-weight: 700; }
  .title-season { top: 236px;  font-size: 90px;  font-weight: 700; letter-spacing: 0.02em; }
  .title-of     { top: 323px;  font-size: 160px; font-weight: 700; letter-spacing: 0.06em; }
  .title-embers { top: 504px;  font-size: 139px; font-weight: 700; color: var(--title-blue); letter-spacing: 0.01em; }
  .subtitle     { top: 703px;  font-size: 34px;  font-weight: 700; letter-spacing: 0.06em; }
  .author       { top: 1030px; font-size: 86px;  font-weight: 700; letter-spacing: 0.03em; }
</style>
</head>
<body>
<main class="cover">
  <div class="field field--ember"></div>
  <div class="field field--band"></div>
  <div class="field field--union"></div>

  <svg class="stars" viewBox="0 0 800 1200" aria-hidden="true">
    <defs>
      <polygon id="star" points="0,-16 3.8,-5.2 15.2,-4.9 6.1,2 9.4,12.9 0,6.5 -9.4,12.9 -6.1,2 -15.2,-4.9 -3.8,-5.2"/>
    </defs>
    <g class="star-arc star-arc--upper">
      <use class="star" href="#star" x="192" y="292"/>
      <use class="star" href="#star" x="145" y="348"/>
      <use class="star" href="#star" x="112" y="410"/>
      <use class="star" href="#star" x="608" y="292"/>
      <use class="star" href="#star" x="655" y="348"/>
      <use class="star" href="#star" x="688" y="410"/>
    </g>
    <g class="star-arc star-arc--lower">
      <use class="star" href="#star" x="133" y="708"/>
      <use class="star" href="#star" x="190" y="771"/>
      <use class="star" href="#star" x="256" y="823"/>
      <use class="star" href="#star" x="330" y="853"/>
      <use class="star" href="#star" x="408" y="864"/>
      <use class="star" href="#star" x="490" y="853"/>
      <use class="star" href="#star" x="565" y="823"/>
      <use class="star" href="#star" x="627" y="771"/>
      <use class="star" href="#star" x="668" y="708"/>
    </g>
  </svg>

  <h1 class="book-title">
    <span class="line title-a">A</span>
    <span class="line title-season">SEASON</span>
    <span class="line title-of">OF</span>
    <span class="line title-embers">EMBERS</span>
  </h1>
  <p class="line subtitle">A NOVEL</p>
  <p class="line author">TOMAS REYVIK</p>
</main>
</body>
</html>
```